Initial website for sport tech startup

We are currently in the R&D phases of our new product. It’s a headband to prevent concussion in the soccer market initially.

We have 2 products, one that’s basic aimed at the youth market and the other more technology driven that’s aimed at the academies and professional market.

Initially the product will launch in the UK

Target Market(s)

Youth soccer players and parents in UK, Soccer Clubs, Federations.

Industry/Entity Type

Sporting Good

Coding

Coded - Design and coding required

Number of Pages Required

5+ page

Requirements
Must have
• Professional style that can be adapted and changed over the coming months.
Nice to have
• Ecommerce ability in the future.

```html
<!DOCTYPE html>
<html lang="en">
<head>
<meta charset="utf-8">
<title>Helmora – Bringing safety to the sports concussion debate</title>
<link href="https://fonts.googleapis.com/css2?family=Montserrat:wght@500;600;700&family=Open+Sans:wght@400;600;700&display=swap" rel="stylesheet">
<style>
:root{
  --blue:#0b5a94;
  --blue-dark:#074a7c;
  --ink:#555b61;
  --heading-grey:#5a5f64;
  --text:#7b7f84;
  --white:#ffffff;
  --footer:#232323;
  --footer-text:#d8d8d8;
}
*{box-sizing:border-box;margin:0;padding:0}
html,body{width:1200px;height:3932px;overflow:hidden}
body{position:relative;background:var(--white);font-family:"Open Sans",Arial,sans-serif;color:var(--text)}
.section{position:absolute;left:0;width:1200px}
.heading{font-family:"Montserrat",Arial,sans-serif;font-weight:700;font-size:40px;color:var(--heading-grey);letter-spacing:.5px;line-height:1}
.heading .accent{color:var(--blue);display:inline-block;border-bottom:6px solid var(--blue);padding-bottom:8px;position:relative}
.heading .accent::after{content:"";position:absolute;right:-2px;bottom:-6px;width:14px;height:22px;background:var(--blue);clip-path:polygon(100% 0,100% 100%,0 100%)}
.heading.light{color:var(--white)}
.btn{display:inline-flex;align-items:center;justify-content:center;background:var(--blue);color:var(--white);font-family:"Open Sans",Arial,sans-serif;font-weight:700;font-size:18px;letter-spacing:.3px;text-decoration:none}

/* top bar */
.topbar{top:0;height:37px;background:var(--blue);color:var(--white);font-family:"Montserrat",Arial,sans-serif;font-weight:600;font-size:17px}
.topbar .contact{position:absolute;left:111px;top:8px;display:flex;gap:12px;align-items:center}
.topbar .login{position:absolute;right:110px;top:8px;display:flex;gap:8px;align-items:center}
.topbar .cart{position:absolute;right:46px;top:0;width:56px;height:37px;background:#2c3e4f;display:flex;align-items:center;justify-content:center}

/* header */
.header{top:37px;height:113px}
.brand{position:absolute;left:111px;top:23px;width:257px;height:60px;border:4px solid var(--blue);display:flex;align-items:center;justify-content:center;font-family:"Montserrat",Arial,sans-serif;font-weight:600;font-size:44px;color:var(--ink);letter-spacing:2px}
.nav{position:absolute;right:110px;top:44px;display:flex;gap:24px;font-family:"Montserrat",Arial,sans-serif;font-weight:500;font-size:17px;color:#5f6468;align-items:center}
.nav .active{color:var(--blue);border-bottom:3px solid var(--blue);padding-bottom:4px;margin-bottom:-7px}

/* hero */
.hero{top:150px;height:546px;background:linear-gradient(90deg,#8a8d8c 0%,#9b9f9a 45%,#7f8784 100%);overflow:hidden}
.hero-photo{position:absolute;left:0;top:18px;width:800px;height:510px;background:linear-gradient(160deg,#5b4a3e 0%,#7b8a5a 55%,#3f7a33 100%);clip-path:polygon(0 0,430px 0,800px 510px,0 510px)}
.hero-band{position:absolute;left:0;top:0}
.hero h1{position:absolute;right:111px;top:68px;text-align:right;font-family:"Montserrat",Arial,sans-serif;font-weight:700;font-size:49px;line-height:63px;color:var(--white)}
.hero .outline{position:absolute;right:111px;top:359px;width:224px;height:68px;border:2px solid var(--white);color:var(--white);font-family:"Open Sans",Arial,sans-serif;font-weight:700;font-size:21px;display:flex;align-items:center;justify-content:center}
.hero .arrows{position:absolute;right:111px;top:474px;display:flex;gap:12px}
.hero .arrows span{width:24px;height:24px;border-radius:50%;background:rgba(255,255,255,.55);display:flex;align-items:center;justify-content:center}

/* welcome */
.welcome{top:696px;height:571px}
.welcome .heading{position:absolute;left:108px;top:80px}
.welcome .copy{position:absolute;left:111px;top:168px;width:490px;font-size:15.5px;line-height:32px}
.welcome .copy p+p{margin-top:32px}
.welcome .btn{position:absolute;left:111px;top:451px;width:157px;height:53px}
.video{position:absolute;left:653px;top:87px;width:436px;height:287px;background:linear-gradient(135deg,#6d7d8c 0%,#3b4e7a 45%,#b83a3a 70%,#5d7fae 100%);box-shadow:0 2px 8px rgba(0,0,0,.35);display:flex;align-items:center;justify-content:center}
.welcome-band{position:absolute;left:0;top:503px}

/* benefits */
.benefits{top:1267px;height:665px;background:linear-gradient(180deg,#4e5552 0%,#3d4443 50%,#49503d 100%)}
.benefits .heading{position:absolute;left:0;width:1200px;text-align:center;top:55px}
.hexgrid{position:absolute;left:111px;top:183px;width:978px;height:420px}
.hex{position:absolute;width:188px;height:214px;clip-path:polygon(50% 0,100% 25%,100% 75%,50% 100%,0 75%,0 25%);display:flex;flex-direction:column;align-items:center;justify-content:center;text-align:center;font-family:"Montserrat",Arial,sans-serif;font-weight:500;font-size:18px;line-height:24px;padding:0 10px}
.hex svg{margin-bottom:12px}
.hex.blue{background:#0d73bf;color:var(--white)}
.hex.white{background:var(--white);color:#444}
.dot{position:absolute;width:60px;height:60px;border-radius:50%}
.dot.blue{background:#0d73bf}.dot.white{background:var(--white)}
.benefits-band{position:absolute;left:0;top:646px}

/* product */
.product{top:1932px;height:648px}
.product .heading{position:absolute;left:645px;top:92px}
.product-visual{position:absolute;left:115px;top:244px;width:465px;height:275px;border-radius:40px 140px 60px 120px;background:linear-gradient(160deg,#4f5256 0%,#2f3134 100%);box-shadow:8px 10px 14px rgba(0,0,0,.25)}
.bullets{position:absolute;left:646px;top:210px;width:455px;list-style:none;font-size:15.5px;line-height:28px}
.bullets li{position:relative;padding-left:31px}
.bullets li+li{margin-top:28px}
.bullets li svg{position:absolute;left:0;top:7px}
.bullets strong{color:#444;font-weight:600}
.product .btn{position:absolute;left:646px;top:500px;width:157px;height:53px}

/* clubs */
.clubs{top:2580px;height:321px}
.clubs-bg{position:absolute;left:0;top:0}
.clubs .heading{position:absolute;left:0;width:1200px;text-align:center;top:70px}
.club-row{position:absolute;left:111px;top:181px;display:flex;gap:21.6px}
.club{width:145px;height:80px;background:var(--white);display:flex;align-items:center;justify-content:center}
.club .badge{width:44px;height:44px;border-radius:50%;background:#c9d3de}
.club .badge.sq{border-radius:6px}

/* articles */
.articles{top:2901px;height:672px}
.article{position:absolute;top:0;width:304px}
.article h3{margin-top:112px;font-family:"Montserrat",Arial,sans-serif;font-weight:700;font-size:30px;color:var(--blue);display:inline-block;border-bottom:6px solid var(--blue);padding-bottom:8px;position:relative}
.article h3::after{content:"";position:absolute;right:-2px;bottom:-6px;width:14px;height:22px;background:var(--blue);clip-path:polygon(100% 0,100% 100%,0 100%)}
.article .pic{position:absolute;top:194px;left:0;width:304px;height:219px}
.article p{position:absolute;top:440px;left:0;width:304px;font-size:15px;line-height:26px}
.article .more{position:absolute;top:556px;left:0;font-weight:700;font-size:17px;color:var(--blue)}
.footer-edge{position:absolute;left:0;top:610px}

/* footer */
.footer{top:3573px;height:359px;background:var(--footer);color:var(--footer-text)}
.fcol{position:absolute;top:75px}
.fcol h4{font-family:"Montserrat",Arial,sans-serif;font-weight:600;font-size:18px;color:var(--white);margin-bottom:20px}
.fcol ul{list-style:none;font-size:14px;line-height:26.5px}
.fcol .row{display:flex;gap:12px;font-size:14px;line-height:20px;margin-bottom:24px}
.fcol .row svg{flex:none;margin-top:3px}
.footer .rule{position:absolute;left:111px;right:111px;top:286px;height:1px;background:#3d3d3d}
.footer .copy{position:absolute;left:111px;top:312px;font-size:14px}
.social{position:absolute;right:111px;top:302px;display:flex;gap:12px}
.social span{width:34px;height:34px;border-radius:50%;border:2px solid #cfcfcf}
</style>
</head>
<body>

<div class="section topbar">
  <div class="contact">
    <svg width="14" height="14" viewBox="0 0 24 24"><path fill="#fff" d="M6.6 10.8a15 15 0 0 0 6.6 6.6l2.2-2.2c.3-.3.7-.4 1-.2 1.1.4 2.3.6 3.6.6.6 0 1 .4 1 1V20c0 .6-.4 1-1 1A17 17 0 0 1 3 4c0-.6.4-1 1-1h3.5c.6 0 1 .4 1 1 0 1.3.2 2.5.6 3.6.1.3 0 .7-.2 1z"/></svg>
    <span>+44 20 0000 0000</span><span>|</span>
    <svg width="16" height="12" viewBox="0 0 16 12"><rect width="16" height="12" rx="1" fill="#fff"/><path d="M1 1l7 5 7-5" stroke="#0b5a94" stroke-width="1.5" fill="none"/></svg>
    <span>hello@helmora.co.uk</span>
  </div>
  <div class="login">
    <svg width="12" height="14" viewBox="0 0 12 14"><rect y="6" width="12" height="8" rx="1" fill="#fff"/><path d="M3 6V4a3 3 0 0 1 6 0v2" stroke="#fff" stroke-width="2" fill="none"/></svg>
    <span>Login</span>
  </div>
  <div class="cart"><svg width="18" height="16" viewBox="0 0 18 16"><path d="M0 1h3l2 9h10l2-7H5" stroke="#fff" stroke-width="2" fill="none"/><circle cx="6" cy="14" r="1.6" fill="#fff"/><circle cx="14" cy="14" r="1.6" fill="#fff"/></svg></div>
</div>

<header class="section header">
  <div class="brand">HELMORA</div>
  <nav class="nav">
    <span class="active">Home</span><span>About</span><span>Product</span><span>Technology</span><span>Clubs</span><span>Team</span><span>Contact</span>
    <svg width="16" height="16" viewBox="0 0 16 16"><circle cx="6.5" cy="6.5" r="5" stroke="#5f6468" stroke-width="2" fill="none"/><path d="M10 10l5 5" stroke="#5f6468" stroke-width="2.4"/></svg>
  </nav>
</header>

<section class="section hero">
  <div class="hero-photo" role="img" aria-label="Close-up of a football player's boot resting on a ball on a stadium pitch"></div>
  <svg class="hero-band" width="1200" height="546" viewBox="0 0 1200 546">
    <polygon points="430,18 470,18 470,60" fill="#0b5a94"/>
    <polygon points="0,480 0,546 800,546 785,528 40,528" fill="#0b5a94"/>
  </svg>
  <h1>BRINGING SAFETY<br>TO THE SPORTS<br>CONCUSSION<br>DEBATE</h1>
  <div class="outline">GET MORE INFO</div>
  <div class="arrows">
    <span><svg width="10" height="12" viewBox="0 0 10 12"><path d="M7 1L2 6l5 5" stroke="#555" stroke-width="2.4" fill="none"/></svg></span>
    <span><svg width="10" height="12" viewBox="0 0 10 12"><path d="M3 1l5 5-5 5" stroke="#555" stroke-width="2.4" fill="none"/></svg></span>
  </div>
</section>

<section class="section welcome">
  <h2 class="heading">WELCOME TO <span class="accent">HELMORA</span></h2>
  <div class="copy">
    <p>Helmora is designing and developing head protection products to reduce the likelihood of concussion when playing sports.</p>
    <p>Exploring and understanding medical insights, material science and composites research, current and former players experiences and governing bodies guidelines has allowed Helmora to develop the safety, style, form and function requirements of a suitable product to bring to market in Q4 2020.</p>
  </div>
  <a class="btn">READ MORE</a>
  <div class="video" role="img" aria-label="Video still of two football players competing for a header">
    <svg width="30" height="34" viewBox="0 0 30 34"><polygon points="2,2 28,17 2,32" fill="#fff"/></svg>
  </div>
  <svg class="welcome-band" width="1200" height="68" viewBox="0 0 1200 68">
    <polygon points="420,48 1160,48 1200,0 1200,68 405,68" fill="#0b5a94"/>
  </svg>
</section>

<section class="section benefits" role="img" aria-label="Faded photo of an injured player being treated on the pitch">
  <h2 class="heading light">PRODUCT <span class="accent">BENEFITS</span></h2>
  <div class="hexgrid">
    <div class="dot white" style="left:64px;top:172px"></div>
    <div class="dot blue" style="left:262px;top:172px"></div>
    <div class="dot white" style="left:459px;top:172px"></div>
    <div class="dot blue" style="left:656px;top:172px"></div>
    <div class="dot white" style="left:854px;top:172px"></div>

    <div class="hex blue" style="left:0;top:0"><svg width="44" height="44" viewBox="0 0 24 24"><path fill="#fff" d="M19.4 13a7.5 7.5 0 0 0 0-2l2.1-1.6-2-3.5-2.5 1a7 7 0 0 0-1.7-1L14.9 3h-4l-.4 2.9a7 7 0 0 0-1.7 1l-2.5-1-2 3.5L6.4 11a7.5 7.5 0 0 0 0 2l-2.1 1.6 2 3.5 2.5-1c.5.4 1.1.7 1.7 1l.4 2.9h4l.4-2.9c.6-.3 1.2-.6 1.7-1l2.5 1 2-3.5zM12.9 15.5a3.5 3.5 0 1 1 0-7 3.5 3.5 0 0 1 0 7z"/></svg>Hightech<br>Polymer</div>
    <div class="hex white" style="left:197px;top:0"><svg width="40" height="44" viewBox="0 0 20 24"><path fill="#0d73bf" d="M10 1L1 4v7c0 6 4 10 9 12 5-2 9-6 9-12V4zm0 3l6 2v5c0 4-3 7-6 9z"/></svg>Safety<br>Tested</div>
    <div class="hex blue" style="left:395px;top:0"><svg width="44" height="44" viewBox="0 0 24 24"><circle cx="12" cy="12" r="10" fill="#fff"/><path fill="#0d73bf" d="M7 6c2 1 3 0 4 2s-1 3 0 5 3 1 3 4-2 3-3 4c-4-1-7-5-7-9 0-2 1-4 3-6zm9 1c2 1 3 2 3 4-2 0-3-1-4-2z"/></svg>Environmentally<br>friendly</div>
    <div class="hex white" style="left:592px;top:0"><svg width="48" height="40" viewBox="0 0 24 20"><path fill="#0d73bf" d="M2 18C4 8 10 2 22 1c0 10-6 16-14 15-2 0-3 0-4 1zm4-3c3-4 7-8 11-10-4 1-8 5-11 10z"/></svg>Light-<br>weight</div>
    <div class="hex blue" style="left:790px;top:0"><svg width="44" height="44" viewBox="0 0 24 24"><path fill="#fff" d="M2 10h4v12H2zm6 0 4-8c2 0 3 1 3 3l-1 4h6c1 0 2 1 2 2l-2 9c0 1-1 2-2 2H8z"/></svg>Comfortable</div>

    <div class="hex white" style="left:0;top:186px"><svg width="30" height="40" viewBox="0 0 16 22"><path fill="#0d73bf" d="M8 1C6 6 2 10 2 14a6 6 0 0 0 12 0c0-4-4-8-6-13z"/></svg>Washable,<br>antibacterial<br>fabric</div>
    <div class="hex blue" style="left:197px;top:186px"><svg width="36" height="44" viewBox="0 0 18 22"><path fill="#fff" d="M1 1h11l5 5v15H1zm4 10h8v1.5H5zm0 3h8v1.5H5zm0 3h8v1.5H5z"/></svg>Personalised<br>options</div>
    <div class="hex white" style="left:395px;top:186px"><svg width="54" height="44" viewBox="0 0 27 22"><circle cx="13.5" cy="5" r="4" fill="#0d73bf"/><circle cx="5" cy="7" r="3" fill="#0d73bf"/><circle cx="22" cy="7" r="3" fill="#0d73bf"/><path fill="#0d73bf" d="M7 21c0-5 3-8 6.5-8S20 16 20 21zm-7-2c0-4 2-6 5-6l1 1c-1 2-1.5 3.5-1.5 5zm27 0c0-4-2-6-5-6l-1 1c1 2 1.5 3.5 1.5 5z"/></svg>Charitable<br>donation</div>
    <div class="hex blue" style="left:592px;top:186px"><svg width="54" height="44" viewBox="0 0 27 22"><circle cx="9" cy="13" r="7" fill="#fff"/><circle cx="9" cy="13" r="2.5" fill="#0d73bf"/><circle cx="20" cy="6" r="5" fill="#fff"/><circle cx="20" cy="6" r="1.8" fill="#0d73bf"/><circle cx="22" cy="17" r="3.5" fill="#fff"/></svg>Giving<br>confidence to<br>parents &amp; users</div>
    <div class="hex white" style="left:790px;top:186px"><svg width="30" height="44" viewBox="0 0 16 24"><path d="M8 2a6 6 0 0 0-4 10.5c1 1 1.5 2 1.5 3.5h5c0-1.5.5-2.5 1.5-3.5A6 6 0 0 0 8 2z" stroke="#0d73bf" stroke-width="2" fill="none"/><rect x="5" y="18" width="6" height="2" fill="#0d73bf"/><rect x="6" y="21" width="4" height="2" fill="#0d73bf"/></svg>Advanced<br>tracking<br>technology</div>
  </div>
  <svg class="benefits-band" width="1200" height="30" viewBox="0 0 1200 30">
    <polygon points="0,0 770,0 755,16 20,16 0,30" fill="#0b5a94"/>
  </svg>
</section>

<section class="section product">
  <h2 class="heading">OUR <span class="accent">PRODUCT</span></h2>
  <div class="product-visual" role="img" aria-label="Illustration of the dark grey protective sports headband"></div>
  <ul class="bullets">
    <li><svg width="16" height="12" viewBox="0 0 16 12"><path d="M1 6l5 5 9-10" stroke="#0b5a94" stroke-width="3" fill="none"/></svg><strong>The first range</strong> of products will be focused on protection, temperature measurement and to reduce the likelihood of concussion and injury. These products will be available in October 2020, and will be suitable for use in soccer.</li>
    <li><svg width="16" height="12" viewBox="0 0 16 12"><path d="M1 6l5 5 9-10" stroke="#0b5a94" stroke-width="3" fill="none"/></svg><strong>The second range</strong> of products will have inbuilt capacity to record performance and allow for a less subjective assessment of concussion. This range will be come available early 2021.</li>
  </ul>
  <a class="btn">READ MORE</a>
</section>

<section class="section clubs">
  <svg class="clubs-bg" width="1200" height="321" viewBox="0 0 1200 321">
    <polygon points="0,0 740,0 756,-22 756,20 1200,20 1200,321 420,321 420,302 0,302" fill="#0b5a94"/>
  </svg>
  <h2 class="heading light">FEATURED &nbsp;<span class="accent">CLUBS</span></h2>
  <div class="club-row">
    <div class="club"><span class="badge"></span></div>
    <div class="club"><span class="badge"></span></div>
    <div class="club"><span class="badge"></span></div>
    <div class="club"><span class="badge sq"></span></div>
    <div class="club"><span class="badge sq"></span></div>
    <div class="club"><span class="badge sq"></span></div>
  </div>
</section>

<section class="section articles">
  <svg style="position:absolute;left:0;top:0" width="1200" height="80" viewBox="0 0 1200 80">
    <polygon points="420,0 460,0 420,70" fill="#0b5a94"/>
  </svg>
  <div class="article" style="left:111px">
    <h3>CONCUSSIONS</h3>
    <div class="pic" role="img" aria-label="Photo of a boy with an ice pack resting on a sofa" style="background:linear-gradient(135deg,#d9e4ec,#5f8fc4 60%,#e8ecf0)"></div>
    <p>A closed head injury due to a direct blow to the head or deceleration of the head from an impulsive force, resulting in transient change in metal status.</p>
    <span class="more">READ MORE</span>
  </div>
  <div class="article" style="left:447px">
    <h3>MEDICAL USES</h3>
    <div class="pic" role="img" aria-label="Photo of a clinician writing notes on a clipboard" style="background:linear-gradient(135deg,#e9c98a,#f3efe6 55%,#d9b27a)"></div>
    <p>A closed head injury due to a direct blow to the head or deceleration of the head from an impulsive force, resulting in transient change in metal status.</p>
    <span class="more">READ MORE</span>
  </div>
  <div class="article" style="left:783px">
    <h3>RESEARCH</h3>
    <div class="pic" role="img" aria-label="Photo of doctors reviewing brain scans on monitors" style="background:linear-gradient(135deg,#cfd6dc,#3d5a70 50%,#e6e9ec)"></div>
    <p>A closed head injury due to a direct blow to the head or deceleration of the head from an impulsive force, resulting in transient change in metal status.</p>
    <span class="more">READ MORE</span>
  </div>
  <svg class="footer-edge" width="1200" height="62" viewBox="0 0 1200 62">
    <polygon points="0,62 400,62 415,50 1160,50 1200,0 1200,62" fill="#232323"/>
  </svg>
</section>

<footer class="section footer">
  <div class="fcol" style="left:111px;width:230px">
    <h4>Contact Us</h4>
    <div class="row"><svg width="10" height="14" viewBox="0 0 10 14"><path fill="#ddd" d="M5 0a5 5 0 0 0-5 5c0 4 5 9 5 9s5-5 5-9a5 5 0 0 0-5-5zm0 7a2 2 0 1 1 0-4 2 2 0 0 1 0 4z"/></svg><span>Ut enim ad minima veniam,<br>quis nostrum exer</span></div>
    <div class="row"><svg width="12" height="12" viewBox="0 0 24 24"><path fill="#ddd" d="M6.6 10.8a15 15 0 0 0 6.6 6.6l2.2-2.2c.3-.3.7-.4 1-.2 1.1.4 2.3.6 3.6.6.6 0 1 .4 1 1V20c0 .6-.4 1-1 1A17 17 0 0 1 3 4c0-.6.4-1 1-1h3.5c.6 0 1 .4 1 1 0 1.3.2 2.5.6 3.6.1.3 0 .7-.2 1z"/></svg><span>+44 20 0000 0000</span></div>
    <div class="row"><svg width="14" height="11" viewBox="0 0 16 12"><rect width="16" height="12" rx="1" fill="#ddd"/><path d="M1 1l7 5 7-5" stroke="#232323" stroke-width="1.5" fill="none"/></svg><span>hello@helmora.co.uk</span></div>
  </div>
  <div class="fcol" style="left:394px">
    <h4>Quick Links</h4>
    <ul><li>Contact</li><li>FAQ</li><li>Investors</li><li>Register My Product</li><li>Product Limited Warranty</li></ul>
  </div>
  <div class="fcol" style="left:617px">
    <h4>Resources</h4>
    <ul><li>Press releases</li><li>In the news</li><li>Related articles</li><li>Research</li><li>Newsletters</li></ul>
  </div>
  <div class="fcol" style="left:805px">
    <h4>Legal &amp; Compliance</h4>
    <ul><li>Privacy and Cookie Notice</li><li>Website Terms of Use</li><li>Sitemap</li><li>Disclaimer</li></ul>
  </div>
  <div class="rule"></div>
  <div class="copy">Copyright © 2020, Helmora .</div>
  <div class="social"><span></span><span></span><span></span></div>
</footer>

</body>
</html>
```